Website design for an Online pastry shop

Website Name : www.lanternandplum.com

Description of the website and its target audience
We are a premium pastry company producing delicious cakes, macarons, cookies, gelato, and other sweet dessert. Our differentiation is that our products are freshly produced with premium quality imported ingredients and one bite into our products set us apart from other bakery shop. We online retail online so as to provide high quality products at a affordable cost. Our products has received raving reviews by many food enthusiast even the hard to please ones. The products contain more natural ingredients and we do not add preservatives. The return rates for our pastry is almost 80%. You only need to try once to be return customers. Our greatest challenge is getting customer to take the first bite. We are so sure of our products that we are going to give people free food tasting.

We are based in China but all our products are developed by award winning chefs from 5 stars hotel. The target customer is woman 16 to 40+ in china. Working class ladies and demand high quality products. A modern, sophisticated and minimalist website

This is a competitive market and image is crucial for such a food ‘conscious ’ orientated customer. They want to feel that they are buying from a reliable company that take great effort to ensure food cleaniness and safety yet affordable price. We make almost 98% of sub ingredients ourselves and we make it by hand.

Style/theme ideas for the web page design
I am looking for a elegant a little rustic, handmade feel yet sophisticated design - one that is easy to the eye yet functional and easy for the user to navigate through. Good play of fonts to give let it feel unique and customised. Black and white is our corporate colours. However, we do not want black background as it does not tease the taste bud. All our colours should come from our products. Customers should be very close to our products. They eat with their eyes first. Black and white is just accent.

Inspirational and competitors websites
http://www.47torte.com/ ( Key competitor )
I like the simple, clean look. The products are the key focus
https://www.pleemo.com/
clean, fresh and different. Attractive with purpose. Feminine
http://quillandbobbin.com/
this has a great layout - lots of information and nicely presented. Very sweet and feminine
http://www.storehavenrow.com/
product features is the focus
http://www.odettevulmers.com/store/
fun, feminine, rustic

Number of pages needed : 6 ( Uncoded PSD design only )
Page descriptions
Home Page - This page will show what makes our products stand out from the competitors and provide an introduction of who we are.
2nd page : Product catalogue
3nd page: Detail Product page with pictures and descriptions. Select products size and add to cart....
4rd page: Brand Story with pictures and descriptions.
5th page Contact Us : Here they can contact or schedule an appointment for free product tasting
6th page : Check out page

Target Market(s)

Female, Asian, Working Class, Office

Industry/Entity Type

Shop

Number of Pages Required

5+ page

Font styles to use
Other font styles liked:
• See packaging

Requirements
Must have
• Please see the project wire frame file " main page.png " or file number 70

```html
<!DOCTYPE html>
<html lang="en">
<head>
<meta charset="utf-8">
<title>Lantern &amp; Plum – Luxurious Pastry</title>
<link rel="stylesheet" href="https://fonts.googleapis.com/css2?family=Mulish:wght@300;400;600;700&family=Great+Vibes&display=swap">
<style>
  :root{
    --ink:#5a5552;
    --ink-soft:#8d8884;
    --ink-faint:#b3afab;
    --accent-red:#e0483b;
    --page:#ffffff;
    --cookie-bg:#e9e9e9;
    --cream:#f8f6f2;
    --lime:#e7e6a2;
    --lime-ink:#6f6c4a;
    --lavender:#f4f2f8;
    --line:#d9d6d2;
    --icon:#c7c4c1;
  }
  *{box-sizing:border-box;margin:0;padding:0}
  html,body{width:1200px;height:3033px;overflow:hidden;background:var(--page)}
  body{position:relative;font-family:"Mulish",Arial,sans-serif;color:var(--ink)}
  .abs{position:absolute}
  a{color:inherit;text-decoration:none}

  /* cookie notice */
  .cookie-bar{left:58px;top:19px;width:1084px;height:52px;background:var(--cookie-bg);
    padding:9px 70px 0 16px;font-size:11.5px;line-height:16px;color:#6e6a67}
  .cookie-bar strong{color:#4a4644}
  .cookie-close{right:18px;top:14px;width:22px;height:22px}

  /* header */
  .site-header{left:58px;top:88px;width:1084px;height:44px}
  .menu-toggle{left:0;top:12px;display:flex;align-items:center;gap:10px;font-size:16px;color:var(--ink-soft)}
  .brand{left:0;right:0;top:8px;text-align:center;font-size:23px;font-weight:600;color:#3d3a38;letter-spacing:.5px}
  .account{right:0;top:12px;font-size:15px;color:var(--ink-faint)}
  .account b{color:var(--ink-soft);font-weight:600}

  /* hero */
  .hero-photo{left:58px;top:155px;width:1084px;height:717px;
    background:radial-gradient(ellipse at 70% 55%,#efe6da 0%,#d9b98e 28%,#a4764b 60%,#6e4a31 100%)}
  .hero-card{left:429px;top:382px;width:340px;height:340px;background:#fff;text-align:center;padding-top:34px}
  .hero-card .kicker{font-size:17px;letter-spacing:6px;color:#bfb4a6;font-weight:300}
  .hero-card .rule{width:270px;height:2px;background:#d7cfc4;margin:10px auto 0}
  .hero-card .headline{font-size:76px;line-height:80px;font-weight:300;color:#c9a378;letter-spacing:2px;margin-top:6px}
  .hero-card .since{font-size:14px;letter-spacing:14px;color:#bfb4a6;margin-top:14px;font-weight:300}
  .hero-card .dots{font-size:10px;letter-spacing:13px;color:#d2c8bc;margin-top:10px}

  /* intro */
  .intro-photo{left:58px;top:898px;width:420px;height:626px;
    background:linear-gradient(160deg,#b89c82 0%,#8a6446 40%,#5c3e29 75%,#8a6a4c 100%)}
  .welcome{left:488px;top:898px;width:654px;height:380px;background:var(--cream);text-align:center;padding-top:110px}
  .welcome h1{font-size:34px;font-weight:400;color:#4d4946}
  .welcome p{font-size:17px;line-height:25px;color:var(--ink-soft);margin:8px auto 0;width:520px}
  .welcome .discover{display:inline-block;margin-top:28px;font-size:17px;color:var(--accent-red)}
  .tart-photo{left:488px;top:1286px;width:654px;height:238px;
    background:radial-gradient(ellipse at 55% 45%,#fafafa 0%,#d8d8d8 40%,#9c9c9c 100%)}

  /* featured */
  .featured{left:58px;top:1533px;width:1084px;height:230px;background:var(--lime);text-align:center;padding-top:38px;color:var(--lime-ink)}
  .featured h2{font-size:36px;font-weight:400;color:#5e5b44}
  .featured p{font-size:17px;line-height:24px;width:560px;margin:18px auto 0}
  .filter{margin-top:24px;display:flex;justify-content:center;gap:46px;font-size:16px}
  .filter .label{margin-right:-24px}
  .filter .active{font-weight:700;color:#4f4c37;text-decoration:underline;text-underline-offset:5px}

  .product{background:radial-gradient(ellipse at 50% 55%,var(--c1) 0%,var(--c2) 45%,#f1eff3 75%)}
  .p-big{left:58px;top:1775px;width:533px;height:363px;--c1:#6b3f26;--c2:#b28d76}
  .p-1{left:600px;top:1775px;width:265px;height:176px;--c1:#f0a21e;--c2:#e6c790}
  .p-2{left:874px;top:1775px;width:268px;height:176px;--c1:#d59a3c;--c2:#efe2cf}
  .p-3{left:600px;top:1960px;width:265px;height:178px;--c1:#3a2b3a;--c2:#e4c98f}
  .p-4{left:874px;top:1960px;width:268px;height:178px;--c1:#e6a98c;--c2:#efe6cf}

  /* newsletter */
  .newsletter{left:58px;top:2150px;width:1084px;height:382px;background:var(--lavender);text-align:center;padding-top:98px}
  .newsletter h2{font-size:33px;font-weight:400;color:#4d4946}
  .newsletter p{font-size:17px;color:var(--ink-soft);margin-top:4px}
  .signup{display:flex;width:431px;height:46px;margin:30px auto 0;border:1px solid #d6d3d9;border-radius:23px;background:#ebe8ee;overflow:hidden}
  .signup input{flex:1;border:0;background:transparent;padding-left:34px;font:14px "Mulish",Arial,sans-serif;color:var(--ink-soft);outline:none}
  .signup input::placeholder{color:#7e7a77}
  .signup button{width:119px;border:0;border-left:1px solid #d0cdd3;background:transparent;font:17px "Mulish",Arial,sans-serif;color:#4d4946}
  .social{display:flex;justify-content:center;gap:19px;margin-top:22px}
  .social span{width:28px;height:28px;background:var(--icon);border-radius:3px}

  /* footer */
  .footer-heading{font-family:"Great Vibes",cursive;font-size:34px;color:#4a4644;line-height:36px}
  .footer-list{list-style:none;font-size:16px;line-height:30px;color:var(--ink-soft)}
  .footer-brand{font-size:22px;font-weight:600;color:#3d3a38}
  .footer-tagline{font-size:14px;color:var(--ink-soft)}
  .address{font-size:16px;line-height:30px;color:var(--ink-soft)}

  .legal{left:0;width:1200px;top:2962px;text-align:center;font-size:15px;color:#6d6966;letter-spacing:.5px}
  .legal .links{margin-top:4px;word-spacing:3px}
</style>
</head>
<body>

<div class="abs cookie-bar">
  Our website uses cookies, as almost all websites do, to help provide you with the best experience we can. Cookies are small text files that are placed on your computer or mobile phone when you browse websites. By continuing to browse the site, you are agreeing to our use of cookies. <strong>Find out more.</strong>
  <svg class="abs cookie-close" viewBox="0 0 22 22" aria-label="Close"><path d="M3 3L19 19M19 3L3 19" stroke="#4a4644" stroke-width="3.2"/></svg>
</div>

<header class="abs site-header">
  <div class="abs menu-toggle">
    <svg width="22" height="16" viewBox="0 0 22 16"><path d="M0 1.5H22M0 8H22M0 14.5H22" stroke="#6e6a67" stroke-width="2.4"/></svg>
    Menu
  </div>
  <div class="abs brand">Lantern &amp; Plum</div>
  <div class="abs account">Sign up / <b>Sign in</b> &nbsp;| Your cart is empty</div>
</header>

<div class="abs hero-photo" role="img" aria-label="Tea set on a wooden board with pastel macarons and a large filled macaron cake"></div>
<div class="abs hero-card">
  <div class="kicker">LUXURIOUS PASTRY</div>
  <div class="rule"></div>
  <div class="headline">HAPPY<br>TASTE</div>
  <div class="rule"></div>
  <div class="since">SINCE 2004</div>
  <div class="dots">• • • • • • • • • •</div>
</div>

<div class="abs intro-photo" role="img" aria-label="Baking ingredients, flour, egg, chocolate and cookies on a rustic wooden table"></div>
<section class="abs welcome">
  <h1>Welcome to Lantern &amp; Plum.</h1>
  <p>We value flavor over fuss. Artisan, handcrafted and other gourmet confections delivered direct to your door.</p>
  <a class="discover" href="#">— Discover our store.</a>
</section>
<div class="abs tart-photo" role="img" aria-label="Meringue tart on a serving plate, in black and white"></div>

<section class="abs featured">
  <h2>Featured products</h2>
  <p>Lorem ipsum dolor sit amet, consectetur adipiscing elit, sed do eiusmod tempor incididunt ut labore et dolore magna aliqua.</p>
  <nav class="filter">
    <span class="label">Filter by :</span>
    <span class="active">Cakes</span>
    <span>Macarons</span>
    <span>Cookies</span>
    <span>Gelato</span>
  </nav>
</section>

<div class="abs product p-big" role="img" aria-label="Chocolate layer cake with chocolate fan decorations"></div>
<div class="abs product p-1" role="img" aria-label="Mango mousse cake"></div>
<div class="abs product p-2" role="img" aria-label="Caramel dome cake ringed with macarons"></div>
<div class="abs product p-3" role="img" aria-label="Blueberry cheesecake"></div>
<div class="abs product p-4" role="img" aria-label="Macaron cake with cream and fruit filling"></div>

<section class="abs newsletter">
  <h2>Join our Newsletter</h2>
  <p>Receive our latest offers. No spam. We respect your privacy.</p>
  <form class="signup">
    <input type="email" placeholder="Enter your address E-mail">
    <button type="button">Subscribe</button>
  </form>
  <div class="social">
    <span aria-label="Feed"></span><span aria-label="Social page"></span><span aria-label="Social updates"></span>
  </div>
</section>

<footer>
  <div class="abs" style="left:117px;top:2584px">
    <div class="footer-heading">Store</div>
    <ul class="footer-list" style="margin-top:2px">
      <li>Cakes</li><li>Macarons</li><li>Cookies</li><li>Gelato</li>
    </ul>
    <div class="footer-heading" style="margin-top:22px">Catalogue</div>
    <div class="footer-heading" style="margin-top:24px">Tasting room</div>
  </div>
  <div class="abs" style="left:373px;top:2584px">
    <div class="footer-heading">About us</div>
    <ul class="footer-list" style="margin-top:2px"><li>Story</li><li>People</li></ul>
    <div class="footer-heading" style="margin-top:20px">Locations</div>
    <div class="footer-heading" style="margin-top:26px">Contact</div>
    <div class="address" style="margin-top:2px">Linwan District,&nbsp; Crescent Tower<br>Guangzhou, China</div>
  </div>
  <div class="abs" style="left:687px;top:2584px">
    <div class="footer-brand">Lantern &amp; Plum</div>
    <div class="footer-tagline">Share the joy of taste.</div>
  </div>

  <div class="abs legal">
    <div>© Lantern &amp; Plum Store. 2015</div>
    <div class="links">Privacy Policy | Shipping &nbsp;| &nbsp;Agreement &nbsp;| &nbsp;Legal &nbsp;| &nbsp;Copyrights &nbsp;| &nbsp;Store Policy</div>
  </div>
</footer>

</body>
</html>
```